Affiliate website design and wireframe

We need a design of an affiliate website for an application we purchased, it is important that you build the website pages according to the developer of the applications specifications (please see attached documents) the developer of the application will configure the pages and add them to the site. Please take special note of his comments below.

We all so need you to create a wire frame so the developer can test everything (http://sketchwire.tolvaro.vn/)

It will be the homepage and about 16 inner pages (please see attached files)
Here is our website http://bluvendmarket.com/affiliate/affiliates/index.php

The version of the software we purchased is the Kivo Partner Hubline version

Comments from the developers

1. I will need the source files of the design (photoshop .psd files and font files if custom fonts are used), since the implementation is closely bound to component sizes (like border width, margin width etc.) and colors. If you own a corporate design manual, it's crucial to send it as well. Also, please, make sure if you use custom fonts, that these allow legal website integration (like google web fonts).

2. Any and every content is controlled via templates. All editing/adding/removing etc. is done here. The template files are essentially html/php documents, they use a template engine called quillo (http://www.quillo.net/) which has it's own language similar to php.

3. .psd files are ideal, because we deal with the specifics of KPX/KPH implementation on a daily basis. Any html/css developed in advance may prove to be a poor choice. You may choose to let an in-house developer do the job, but experience wise this is more costly, since he will not be accustomed to the template/functionality systems of KPX/KPH.

4. I will need the source files of the design (photoshop .psd files and font files if custom fonts are used), since the implementation is closely bound to component sizes (like border width, margin width etc.) and colors. If you own a corporate design manual, it's crucial to send it as well. Also, please, make sure if you use custom fonts, that these allow legal website integration (like google web fonts).

Regards,

Dorek Hanval
Multimedia Design

We prefer illustrations more than pictures of real people.

This is the home page, it is asking for Merchant and Affiliate sign up, not just affiliate.

http://bluvendmarket.com/affiliate/index.php

Please note the home page features both Merchant and Affiliate sign up

We are looking for illustration design not just stock images

Please remember the search menu that searches for the available programs, see the example we gave you, look at the search menu at the top of the page http://www.tradelumo.com/

We are reviewing everything, no need to send more designs

Target Market(s)

Natural Products Manufacturers
Natural products Sales reps
Natural Products Bloggers
Social Marketing

Industry/Entity Type

Software

Requirements
Must have
• 1. All links on pages should go to the appropriate pages.
2. Colors can be based on our logo design (look at the attachments)
3. Here is our website http://bluvendmarket.com/affiliate/affiliates/index.php
4. We have attached a drawing of how we think the homepage concept should follow.
5. Main concept of design, is trying to show our sales people (Affiliates) are doing multiple things to advertise and sell the merchants products.(see logo)
6. Need to be able to edit all text and images.
7. Our target audience is Natural product sales people (Advertisers, bloggers, ext) and natural product manufacturers.
8. You can speak to the company who made the application, through live chat, on there website http://www.kivopartnerhubline.com/
Nice to have
• See Attached Documents.
site should take up whole website pages
Look For fun Illustrated Website, one of the better ones we have seen is http://www.tradelumo.com/index.cfm
Should not have
• Please look very carefully at developers comment above.

```html
<!DOCTYPE html>
<html lang="en">
<head>
<meta charset="utf-8">
<title>Bluvend Market – Affiliate Program</title>
<link rel="stylesheet" href="https://fonts.googleapis.com/css2?family=Roboto:wght@300;400;500;700&display=swap">
<style>
:root{
  --green:#6aa51f;
  --green-dark:#4f8214;
  --navy:#23324a;
  --ink:#333333;
  --muted:#777777;
  --light-band:#eef0ee;
  --hero-band:#e6e8e6;
  --rule:#dddddd;
  --footer:#3b3d3c;
  --footer-bottom:#2c2e2d;
  --footer-text:#b9bcb9;
  --white:#ffffff;
}
*{box-sizing:border-box;margin:0;padding:0}
html,body{width:1200px;height:2356px;overflow:hidden}
body{font-family:"Roboto",Arial,sans-serif;color:var(--ink);background:var(--white);position:relative}
a{color:inherit;text-decoration:none}
.btn{display:inline-block;background:var(--green);color:var(--white);font-weight:500;text-transform:uppercase;border-radius:3px}

/* header */
.site-header{height:160px;position:relative;border-bottom:1px solid var(--rule)}
.account-links{position:absolute;right:24px;top:18px;display:flex;gap:8px}
.account-links a{font-size:14px;font-weight:500;color:var(--white);padding:9px 22px;border-radius:3px}
.account-links .login{background:var(--green)}
.account-links .signup{background:var(--navy)}
.brand{position:absolute;left:22px;top:30px;display:flex;align-items:center;gap:12px}
.brand-mark{width:44px;height:44px;border-radius:50%;background:var(--green)}
.brand-name{font-size:30px;font-weight:700;color:var(--green);letter-spacing:.5px}
.main-nav{position:absolute;right:30px;top:104px;display:flex;gap:34px;font-size:14px;color:var(--muted)}
.main-nav a.active{color:var(--green);border-bottom:2px solid var(--green);padding-bottom:6px}

/* hero */
.hero{height:440px;background:var(--hero-band);position:relative}
.hero-copy{position:absolute;left:90px;top:88px;width:470px}
.hero-copy h1{font-size:44px;font-weight:400;color:var(--ink);margin-bottom:14px}
.hero-copy p{font-size:19px;line-height:27px;color:#555;font-weight:300}
.hero-copy .btn{margin-top:22px;font-size:17px;text-transform:none;padding:14px 26px}
.hero-dots{position:absolute;left:90px;top:395px;display:flex;gap:12px}
.hero-dots span{width:10px;height:10px;border-radius:50%;background:#b8bab8}
.hero-dots span.on{background:var(--green)}
.hero-art{position:absolute;left:640px;top:12px;width:520px;height:416px;border-radius:8px;
  background:radial-gradient(circle at 50% 50%,#cfd6c8 0,#dfe3dc 45%,#e6e8e6 75%)}

/* features */
.features{height:448px;display:flex;justify-content:center;gap:80px;padding-top:56px}
.feature{width:290px;text-align:center}
.feature-icon{width:120px;height:120px;margin:0 auto 24px;display:block}
.feature h3{font-size:20px;font-weight:400;line-height:26px;color:var(--ink);margin-bottom:12px}
.feature p{font-size:14px;line-height:21px;color:var(--muted);font-weight:300;min-height:44px}
.feature .btn{margin-top:22px;font-size:12px;padding:9px 20px}

/* how it works */
.how-it-works{height:472px;background:var(--light-band);border-top:1px solid var(--rule);padding:80px 0 0}
.how-it-works h2,.join h2{font-size:46px;font-weight:300;text-align:center;color:var(--ink)}
.how-body{width:1040px;margin:50px auto 0;font-size:16px;line-height:24px;color:#555;font-weight:300}
.how-body ul{margin:14px 0 14px 50px;list-style:none}
.how-body li{position:relative;margin-bottom:4px}
.how-body li::before{content:"";position:absolute;left:-24px;top:9px;width:7px;height:7px;border-radius:50%;background:var(--green)}

/* join */
.join{height:380px;padding-top:64px;text-align:center;border-top:1px solid var(--rule)}
.join p{width:560px;margin:22px auto 0;font-size:19px;line-height:28px;color:#555;font-weight:300}
.join .btn{margin-top:32px;font-size:15px;text-transform:none;padding:13px 26px}

/* footer */
.site-footer{position:absolute;left:0;top:1900px;width:1200px;height:400px;background:var(--footer);
  display:flex;gap:0;padding:50px 0 0 40px}
.footer-col{width:290px}
.footer-col h4{font-size:17px;font-weight:500;color:var(--green);text-transform:uppercase;margin-bottom:26px}
.footer-col a{display:block;font-size:15px;color:var(--footer-text);line-height:24px;font-weight:300}
.social{display:flex;gap:12px;margin-bottom:30px}
.social span{width:46px;height:46px;border-radius:50%;background:#8e918e}
.stores{display:flex;gap:12px}
.stores span{width:128px;height:42px;border-radius:6px;background:#111111;border:1px solid #777}
.copyright{position:absolute;left:0;top:2300px;width:1200px;height:56px;background:var(--footer-bottom);
  color:#8a8d8a;font-size:13px;text-align:center;line-height:56px}
</style>
</head>
<body>

<header class="site-header">
  <div class="account-links">
    <a class="login" href="#">LOGIN</a>
    <a class="signup" href="#">SIGNUP</a>
  </div>
  <a class="brand" href="#"><span class="brand-mark"></span><span class="brand-name">BLUVEND MARKET</span></a>
  <nav class="main-nav">
    <a class="active" href="#">HOME</a>
    <a href="#">ABOUT US</a>
    <a href="#">SERVICES</a>
    <a href="#">AFFILIATES</a>
    <a href="#">CONTACT US</a>
  </nav>
</header>

<section class="hero">
  <div class="hero-copy">
    <h1>Start Making Money Now!</h1>
    <p>There is no charge to join our Affiliate Program.<br>We pay commissions for all sales you referred.<br>Earn up to 30% commissions</p>
    <a class="btn" href="#">Affiliates Signup</a>
  </div>
  <div class="hero-dots"><span class="on"></span><span></span><span></span><span></span></div>
  <div class="hero-art" role="img" aria-label="Illustration of an affiliate at the centre of a hub, linked to social, phone, email, web and chat channels"></div>
</section>

<section class="features">
  <div class="feature">
    <svg class="feature-icon" viewBox="0 0 120 120"><circle cx="60" cy="60" r="56" fill="#6aa51f"/><text x="60" y="70" font-family="Roboto,Arial,sans-serif" font-size="30" font-weight="700" fill="#fff" text-anchor="middle">60%</text><path d="M36 86h48" stroke="#fff" stroke-width="3"/></svg>
    <h3>Earn up to 50% commission<br>for all products!</h3>
    <p>Not only can you join our team and help spread the word about your favorite products</p>
    <a class="btn" href="#">Read More</a>
  </div>
  <div class="feature">
    <svg class="feature-icon" viewBox="0 0 120 120"><circle cx="60" cy="60" r="56" fill="#6aa51f"/><text x="60" y="74" font-family="Roboto,Arial,sans-serif" font-size="38" font-weight="700" fill="#fff" text-anchor="middle">$$$</text></svg>
    <h3>High Conversion Rate<br>= More Money</h3>
    <p>Our website and plans generate one of the highest conversion rates in the industry.</p>
    <a class="btn" href="#">Read More</a>
  </div>
  <div class="feature">
    <svg class="feature-icon" viewBox="0 0 120 120"><circle cx="60" cy="60" r="56" fill="#6aa51f"/><rect x="33" y="33" width="54" height="54" rx="6" fill="none" stroke="#fff" stroke-width="5" transform="rotate(45 60 60)"/><path d="M44 60h28M62 48l12 12-12 12" fill="none" stroke="#fff" stroke-width="6" stroke-linecap="round" stroke-linejoin="round"/></svg>
    <h3>Long cookie<br>duration</h3>
    <p>If a customer comes from your site to ours, and then comes back to purchase six months later</p>
    <a class="btn" href="#">Read More</a>
  </div>
</section>

<section class="how-it-works">
  <h2>How Does It Work?</h2>
  <div class="how-body">
    <p>It couldn't be simpler! We've streamlined our entire affiliate process to ensure ease of use, while still maintaining extremely accurate affiliate tracking. The process is as follows:</p>
    <ul>
      <li>Visitor clicks on an affiliate link on your site or in an email.</li>
      <li>The visitor's IP is logged and a cookie is placed in their browser for tracking purposes.</li>
      <li>The visitor browses our site, and may decide to order.</li>
      <li>If the visitor orders (the order need not be placed during the same browser session—cookies and IPs are stored indefinitely), the order will be registered as a sale for you.</li>
      <li>We will review and approve the sale.</li>
      <li>You will receive commission payouts.</li>
    </ul>
    <p>That's it! You send us business, we send you money!</p>
  </div>
</section>

<section class="join">
  <h2>Ready to Join?</h2>
  <p>Signing up and getting your account configured couldn't be easier. You can be referring business our way in as little as five minutes.</p>
  <a class="btn" href="#">Join Now!</a>
</section>

<footer class="site-footer">
  <div class="footer-col">
    <h4>About Us</h4>
    <a href="#">Company</a><a href="#">Contact us</a><a href="#">Privacy Policy</a>
  </div>
  <div class="footer-col">
    <h4>Affiliates</h4>
    <a href="#">Affiliates Information</a><a href="#">Affiliate link formats</a>
  </div>
  <div class="footer-col">
    <h4>Merchants</h4>
    <a href="#">Merchants Login</a><a href="#">Integration methods</a><a href="#">API Reference</a><a href="#">Services and Tools</a><a href="#">Find Affiliate Pro</a>
  </div>
  <div class="footer-col">
    <h4>Stay In Touch</h4>
    <div class="social"><span></span><span></span><span></span><span></span></div>
    <div class="stores"><span></span><span></span></div>
  </div>
</footer>
<div class="copyright">All Rights Reserved Copyright © 2014</div>

</body>
</html>
```